Crit postcard design

I am in charge of getting a postcard 5x7 designed for 14 artists having a gallery exhibition. We would like to use our
photo(s) with the 14 names on the front. Back of card would have gallery information.
Am sending jpeg of a past card, four images to choose from and the text for back of card.

Artists

```html
<!DOCTYPE html>
<html lang="en">
<head>
<meta charset="utf-8">
<title>The Easel Circle – Postcard</title>
<link rel="stylesheet" href="https://fonts.googleapis.com/css2?family=Alfa+Slab+One&family=Archivo+Narrow:wght@500;700&family=Libre+Baskerville:ital,wght@0,700;1,400;1,700&family=Arimo:wght@400&display=swap">
<style>
  :root {
    --navy: #2e3468;
    --ink: #1a1a22;
    --panel: #c9d0d6;
    --banner: #dde1e5;
    --white: #ffffff;
    --text-grey: #3d4250;
  }
  * { margin: 0; padding: 0; box-sizing: border-box; }
  html, body { width: 801px; height: 1200px; overflow: hidden; background: var(--panel); }
  .postcard { position: relative; width: 801px; height: 1200px; overflow: hidden; background: var(--panel); }

  .hero-photo {
    position: absolute; left: 0; top: 0; width: 801px; height: 605px;
    background:
      radial-gradient(circle at 30% 70%, #f2d23a 0 8%, transparent 20%),
      radial-gradient(circle at 55% 35%, #1f2f78 0 10%, transparent 28%),
      radial-gradient(circle at 15% 25%, #c7302b 0 6%, transparent 18%),
      radial-gradient(circle at 70% 75%, #3a3530 0 12%, transparent 30%),
      linear-gradient(135deg, #eeeae4 0%, #c9c3ba 45%, #8c8378 100%);
  }

  .artist-banner { position: absolute; left: 553px; top: 0; width: 236px; height: 440px; }
  .banner-text {
    position: absolute; left: 553px; top: 12px; width: 236px;
    text-align: center; color: var(--navy);
    font-family: "Archivo Narrow", sans-serif; font-weight: 700; text-transform: uppercase;
    line-height: 1.02;
  }
  .count { display: flex; align-items: center; justify-content: center; gap: 8px; margin-bottom: 8px; }
  .count-number { font-family: "Alfa Slab One", serif; font-size: 72px; color: var(--ink); line-height: 1; }
  .count-label { background: var(--navy); color: var(--white); font-size: 24px; padding: 4px 6px; letter-spacing: 1px; }
  .names span { display: inline-block; margin: 0 3px; }
  .n-lg { font-size: 34px; }
  .n-md { font-size: 26px; }
  .n-sm { font-size: 19px; }

  .back-divider { position: absolute; left: 400px; top: 612px; height: 580px; border-left: 3px dashed var(--navy); }
  .info { position: absolute; left: 0; top: 605px; width: 400px; text-align: center; }
  .presenter-tag {
    width: 166px; margin: 0 auto; background: var(--navy); color: var(--white);
    font-family: "Libre Baskerville", serif; font-size: 15px; line-height: 1.5; padding: 22px 8px 14px;
  }
  .show-title { font-family: "Libre Baskerville", serif; font-weight: 700; font-size: 40px; color: var(--ink); margin-top: 18px; }
  .show-dates { font-family: "Libre Baskerville", serif; font-style: italic; font-weight: 700; color: var(--navy); font-size: 21px; line-height: 1.35; margin-top: 8px; }
  .dot-rule { width: 390px; margin: 20px 0 22px 10px; border-top: 6px dotted var(--navy); }
  .gallery-details { font-family: "Arimo", sans-serif; font-size: 15px; line-height: 1.45; color: var(--text-grey); }
  .hours { margin-top: 20px; padding: 0 40px; }
</style>
</head>
<body>
<main class="postcard">
  <div class="hero-photo" role="img" aria-label="Photograph of a paintbrush resting on tangled drips of colourful paint"></div>

  <svg class="artist-banner" viewBox="0 0 236 440" aria-hidden="true">
    <polygon points="0,0 236,0 236,440 118,385 0,440" fill="var(--banner)"/>
  </svg>
  <div class="banner-text">
    <div class="count"><span class="count-number">14</span><span class="count-label">Painters</span></div>
    <div class="names">
      <span class="n-sm">Varela</span><span class="n-md">Dunn</span><br>
      <span class="n-md">Colfax</span><br>
      <span class="n-lg">Carrow</span><br>
      <span class="n-sm">Tully</span><span class="n-sm">Jessop</span><br>
      <span class="n-md">Greaves</span><br>
      <span class="n-sm">Lin</span><span class="n-md">Orwick</span><br>
      <span class="n-sm">Lassen</span><br>
      <span class="n-lg">Oberly</span><br>
      <span class="n-sm">Ruiz</span><span class="n-md">Norgaard</span>
    </div>
  </div>

  <div class="back-divider"></div>
  <section class="info">
    <div class="presenter-tag">Gallery Lowline<br>presents an exhibition<br>by</div>
    <h1 class="show-title">“The Easel Circle”</h1>
    <p class="show-dates">September 28th – October 31, 2015<br>Reception – Friday, October 2, 5-8pm</p>
    <div class="dot-rule"></div>
    <address class="gallery-details" style="font-style:normal">
      Gallery Lowline<br>
      Harbor Row Shops, 4120 Quarry Lane<br>
      Fairmont, Virginia 22918<br>
      555-014-2290<br>
      info@gallerylowline.org<br>
      www.gallerylowline.org
    </address>
    <p class="gallery-details hours">Gallery Hours: M-F 10:00am-6:00pm, Sat 12pm-2pm. Parking is available in garages, on nearby streets and in public lots (free on weekends and after 4pm weekdays)</p>
  </section>
</main>
</body>
</html>
```